Blue Finch Journeys

We are a predominantly online travel agency with high-end (first/business class) clients. I'm looking to either have our existing logo revamped or a new logo created with business card layout. I prefer to work with existing logo if possible so it remains familiar with existing clientele. I have uploaded a yellow business card layout showing icons on one side of the card. I would like to keep my existing colours, not yellow. could the company name/tag line go over the icons?
Business
Colette Draybin
Director
(I.A.T.A. 07815536)
(Vonsarel Pty. Ltd) ABN 61 574 203 819
412/58 Calderwood Street
Potts Point | NSW 2577 | Australia
www.bluefinchjourneys.com.au
m: + 61 (0) 455 318 906
t: + 61 (0) 2 8471 2063
e: colette@bluefinchjourneys.com.au

```html
<!DOCTYPE html>
<html lang="en">
<head>
<meta charset="utf-8">
<title>Blue Finch Journeys – Business Card</title>
<link rel="stylesheet" href="https://fonts.googleapis.com/css2?family=Cookie&family=Roboto:ital,wght@0,400;0,500;1,400&display=swap">
<style>
  :root {
    --backdrop: #2a2a2a;
    --card-white: #fdfefe;
    --card-tint: #f1f6fb;
    --brand-tone: #d6e5f2;
    --ink: #1c3550;
    --text-grey: #4a4f55;
    --rule: #7f97ae;
  }
  * { box-sizing: border-box; margin: 0; padding: 0; }
  html, body {
    width: 1200px; height: 960px; overflow: hidden;
    background: var(--backdrop);
    font-family: "Roboto", Arial, sans-serif;
  }
  .canvas { position: relative; width: 1200px; height: 960px; }

  .card {
    position: absolute; width: 600px; height: 343px;
    box-shadow: 2px 3px 4px rgba(0,0,0,0.6);
    overflow: hidden;
  }
  .card--front { left: 314px; top: 113px; background: var(--card-white); }
  .card--back  { left: 311px; top: 472px; background: var(--card-tint); }

  .back-pattern {
    position: absolute; inset: 0;
    background: linear-gradient(90deg, #eaf2f9, #f6f9fc 50%, #eaf2f9);
  }

  .brand {
    position: absolute; width: 250px; height: 96px;
    display: flex; flex-direction: column; align-items: center; justify-content: center;
    background: var(--brand-tone);
  }
  .card--front .brand { left: 48px; top: 45px; }
  .card--back .brand { left: 156px; top: 122px; width: 286px; height: 110px; }
  .brand__name {
    font-weight: 400; font-size: 24px; color: var(--ink); white-space: nowrap;
    padding-bottom: 5px; border-bottom: 1px solid var(--rule);
  }
  .card--back .brand__name { font-size: 27px; }
  .brand__tagline {
    font-size: 12px; color: var(--text-grey); letter-spacing: 0.5px; margin-top: 5px;
  }
  .card--back .brand__tagline { font-size: 13px; }

  .edge-tab {
    position: absolute; left: 0; top: 207px; width: 16px; height: 51px;
    background: var(--brand-tone);
  }

  .holder { position: absolute; left: 48px; top: 198px; }
  .holder__name {
    font-family: "Cookie", cursive; font-size: 44px; line-height: 44px; color: var(--ink);
  }
  .holder__title {
    margin-left: 22px; font-size: 15px; font-weight: 500; color: var(--text-grey);
  }
  .holder__reg {
    margin-left: 22px; margin-top: 8px; font-size: 11.5px; line-height: 16px; color: var(--text-grey);
  }

  .contact { position: absolute; left: 322px; top: 161px; color: var(--text-grey); font-size: 13.5px; }
  .contact__address { line-height: 18px; margin-bottom: 10px; }
  .contact__list { list-style: none; }
  .contact__item { display: flex; align-items: center; height: 19px; white-space: nowrap; }
  .contact__icon { width: 13px; height: 13px; margin-right: 9px; fill: var(--ink); flex: none; }

  .back-web {
    position: absolute; left: 0; right: 0; top: 262px; text-align: center;
    font-style: italic; font-size: 15px; letter-spacing: 3px; color: var(--text-grey);
  }
</style>
</head>
<body>
<main class="canvas">
  <section class="card card--front" aria-label="Business card front">
    <div class="brand">
      <span class="brand__name">Blue Finch Journeys</span>
      <span class="brand__tagline">first &amp; business class travel</span>
    </div>
    <div class="edge-tab" role="img" aria-label="Small striped edge decoration"></div>
    <div class="holder">
      <p class="holder__name">Colette Draybin</p>
      <p class="holder__title">Director</p>
      <p class="holder__reg">(I.A.T.A. 07815536)<br>(Vonsarel Pty. Ltd) ABN 61 574 203 819</p>
    </div>
    <div class="contact">
      <p class="contact__address">412/58 Calderwood Street<br>Potts Point | NSW 2577 | Australia</p>
      <ul class="contact__list">
        <li class="contact__item">
          <svg class="contact__icon" viewBox="0 0 16 16"><path d="M4 0h8v16H4zM5.5 2v10h5V2z"/></svg>m: + 61 (0) 455 318 906
        </li>
        <li class="contact__item">
          <svg class="contact__icon" viewBox="0 0 16 16"><path d="M3 1l3 3-1.5 2c1 2 3 4 5 5l2-1.5 3 3-2 2C7 14 2 9 1 3z"/></svg>t: + 61 (0) 2 8471 2063
        </li>
        <li class="contact__item">
          <svg class="contact__icon" viewBox="0 0 16 16"><path d="M1 4h14v9H1zM2 5l6 4 6-4v-.5H2z" fill-rule="evenodd"/></svg>e: colette@bluefinchjourneys.com.au
        </li>
        <li class="contact__item">
          <svg class="contact__icon" viewBox="0 0 16 16"><circle cx="8" cy="8" r="7"/><path d="M4 5l3 1 1 3-2 2 1 3M10 3l1 2 3 1" stroke="#fff" stroke-width="1.2" fill="none"/></svg>www.bluefinchjourneys.com.au
        </li>
      </ul>
    </div>
  </section>

  <section class="card card--back" aria-label="Business card back">
    <div class="back-pattern" role="img" aria-label="Soft pale blue vertical stripe pattern"></div>
    <div class="brand">
      <span class="brand__name">Blue Finch Journeys</span>
      <span class="brand__tagline">first &amp; business class travel</span>
    </div>
    <p class="back-web">www.bluefinchjourneys.com.au</p>
  </section>
</main>
</body>
</html>
```